Menu Design Project

We are a cafe in italy our name is "Bright Corvella Cafe & Food"

We need a new menu we offer cafes and snacks.

our web site is brightcorvella.com you can find there our logo.

We need something clean to print so we can offer to our clients a good menu.

Target Market(s)

cafe clients

Industry/Entity Type

Cafe

Requirements
Must have
• - Nice design
- Our logo
- Demo text so we can write our text

```html
<!DOCTYPE html>
<html lang="en">
<head>
<meta charset="utf-8">
<title>Bright Corvella Cafe &amp; Food — Menu</title>
<link rel="stylesheet" href="https://fonts.googleapis.com/css2?family=Didact+Gothic&family=Dancing+Script:wght@500&display=swap">
<style>
  :root {
    --page: #ffffff;
    --stone: #b3aba6;
    --ink: #1a1a1a;
    --heading: #6b4620;
    --band-dark: #151517;
    --band-stripe: #26262a;
    --band-edge: #050505;
    --accent: #e89a2c;
    --white: #ffffff;
    --dot-dark: #3c3c3c;
  }
  * { box-sizing: border-box; margin: 0; padding: 0; }
  html, body { width: 1000px; height: 1200px; overflow: hidden; background: var(--page); }
  body { position: relative; font-family: "Didact Gothic", "Century Gothic", sans-serif; }

  .spread {
    position: absolute; left: 104px; width: 782px; height: 553px;
    background: var(--stone); overflow: hidden;
  }
  .spread--front { top: 32px; }
  .spread--inside { top: 604px; }

  .band {
    position: absolute; left: 0; top: 398px; width: 100%; height: 155px;
    border-top: 4px solid var(--band-edge);
    background: repeating-linear-gradient(90deg, var(--band-dark) 0 14px, var(--band-stripe) 14px 26px);
  }
  .band::after {
    content: ""; position: absolute; inset: 0;
    background: linear-gradient(180deg, rgba(0,0,0,0) 0%, rgba(0,0,0,0.35) 100%);
  }

  .menu-column { position: absolute; top: 34px; width: 316px; }
  .menu-column--left { left: 33px; }
  .menu-column--right { left: 429px; }

  .menu-item { margin-bottom: 17px; }
  .menu-item__name {
    font-size: 11.5px; color: var(--heading); text-transform: uppercase;
    letter-spacing: 0.2px; line-height: 14px; margin-bottom: 1px;
  }
  .menu-item__desc {
    font-size: 9.6px; color: var(--ink); line-height: 10.6px; text-align: justify;
  }

  .pattern-panel {
    position: absolute; left: 406px; top: 0; width: 376px; height: 398px;
    background: radial-gradient(circle at 50% 45%, #6f6a67 0%, #5a5654 60%, #4e4b49 100%);
  }

  .icon-tile {
    position: absolute; top: 340px; width: 112px; height: 112px;
    background: #000; padding: 12px; z-index: 2;
  }
  .icon-tile--left { left: 128px; }
  .icon-tile--right { left: 523px; }
  .icon-tile__frame {
    width: 100%; height: 100%; border: 3px solid var(--white);
    display: flex; align-items: center; justify-content: center;
  }
  .icon-tile__frame svg { width: 62px; height: 62px; }

  .brand-mark {
    font-family: "Didact Gothic", sans-serif; color: var(--accent);
    font-size: 13px; line-height: 15px; text-align: center;
  }

  .category {
    position: absolute; top: 466px; width: 340px; text-align: center; z-index: 2;
  }
  .category--left { left: 18px; }
  .category--right { left: 413px; }
  .category__title {
    font-family: "Dancing Script", cursive; font-weight: 500;
    font-size: 25px; color: var(--accent); line-height: 30px;
  }
  .category__desc {
    font-size: 9.6px; color: var(--white); line-height: 11px; margin-top: 2px;
  }
</style>
</head>
<body>

<section class="spread spread--front" aria-label="Menu cover spread">
  <div class="menu-column menu-column--left">
    <article class="menu-item">
      <h3 class="menu-item__name">Pepper Steak | $9</h3>
      <p class="menu-item__desc">7 oz. NZ sirloin steak coated with cracked peppercorn. Served with smashed potatoes and fresh vegetables.</p>
    </article>
    <article class="menu-item">
      <h3 class="menu-item__name">Twisted Mac, Chicken &amp; Cheese | $60</h3>
      <p class="menu-item__desc">A grilled chicken breast tops off twisted cavatappi pasta tossed in a lightly spiced 3-cheese sauce, with garlic roasted red peppers and Romano parsley bread crumbs. Served with a side of garlic toast.</p>
    </article>
    <article class="menu-item">
      <h3 class="menu-item__name">Grilled Salmon Fillet | $45</h3>
      <p class="menu-item__desc">An 8 oz. fillet grilled and topped with a Meriot-garlic butter and served with smashed potatoes &amp; fresh vegetables.</p>
    </article>
    <article class="menu-item">
      <h3 class="menu-item__name">Grilled Chicken Masala | $70</h3>
      <p class="menu-item__desc">A tender marinated boneless chicken breast fire grilled and served on a bed of thin spaghetti pasta with a hint of garlic, parmesan cheese, mushrooms and fresh spinach leaves. Topped with mushrooms and a rich Marsala wine sauce, served with fresh vegetables</p>
    </article>
    <article class="menu-item">
      <h3 class="menu-item__name">Fish &amp; Chips | $90</h3>
      <p class="menu-item__desc">Fillet of fish dipped in our special batter and deep-fried to a golden brown. Served with french fries.</p>
    </article>
  </div>

  <div class="pattern-panel" role="img" aria-label="Cover pattern of dark grey polka dots on stone"></div>

  <div class="band"></div>

  <div class="icon-tile icon-tile--left">
    <div class="icon-tile__frame">
      <svg viewBox="0 0 64 64" aria-label="Desserts icon" role="img">
        <rect x="8" y="10" width="16" height="30" rx="7" fill="#fff" transform="rotate(-12 16 25)"/>
        <line x1="20" y1="40" x2="22" y2="54" stroke="#fff" stroke-width="3" stroke-linecap="round"/>
        <circle cx="40" cy="22" r="8" fill="#fff"/>
        <circle cx="50" cy="28" r="7" fill="#fff"/>
        <path d="M32 30 L56 32 L40 58 Z" fill="#fff"/>
      </svg>
    </div>
  </div>

  <div class="icon-tile icon-tile--right">
    <div class="icon-tile__frame">
      <p class="brand-mark">Bright<br>Corvella</p>
    </div>
  </div>

  <div class="category category--left">
    <h2 class="category__title">classification here</h2>
    <p class="category__desc">Fillet of fish dipped in our special batter and deep-fried to a golden brown. Served with french fries. (description)</p>
  </div>
</section>

<section class="spread spread--inside" aria-label="Menu inside spread">
  <div class="menu-column menu-column--left">
    <article class="menu-item">
      <h3 class="menu-item__name">Pepper Steak | $9</h3>
      <p class="menu-item__desc">7 oz. NZ sirloin steak coated with cracked peppercorn. Served with smashed potatoes and fresh vegetables.</p>
    </article>
    <article class="menu-item">
      <h3 class="menu-item__name">Twisted Mac, Chicken &amp; Cheese | $60</h3>
      <p class="menu-item__desc">A grilled chicken breast tops off twisted cavatappi pasta tossed in a lightly spiced 3-cheese sauce, with garlic roasted red peppers and Romano parsley bread crumbs. Served with a side of garlic toast.</p>
    </article>
    <article class="menu-item">
      <h3 class="menu-item__name">Grilled Salmon Fillet | $45</h3>
      <p class="menu-item__desc">An 8 oz. fillet grilled and topped with a Meriot-garlic butter and served with smashed potatoes &amp; fresh vegetables.</p>
    </article>
    <article class="menu-item">
      <h3 class="menu-item__name">Grilled Chicken Masala | $70</h3>
      <p class="menu-item__desc">A tender marinated boneless chicken breast fire grilled and served on a bed of thin spaghetti pasta with a hint of garlic, parmesan cheese, mushrooms and fresh spinach leaves. Topped with mushrooms and a rich Marsala wine sauce, served with fresh vegetables</p>
    </article>
    <article class="menu-item">
      <h3 class="menu-item__name">Fish &amp; Chips | $90</h3>
      <p class="menu-item__desc">Fillet of fish dipped in our special batter and deep-fried to a golden brown. Served with french fries.</p>
    </article>
  </div>

  <div class="menu-column menu-column--right">
    <article class="menu-item">
      <h3 class="menu-item__name">Iced Mocha | $4</h3>
      <p class="menu-item__desc">This served with ice. To make an iced Mocha, add chocolate to bottom of the glass, add espresso and mix well, then add milk.</p>
    </article>
    <article class="menu-item">
      <h3 class="menu-item__name">Cappucino | $6</h3>
      <p class="menu-item__desc">Coffee made with milk that has been frothed up with pressurezed steam.</p>
    </article>
    <article class="menu-item">
      <h3 class="menu-item__name">Iced Mocha | $4</h3>
      <p class="menu-item__desc">This served with ice. To make an iced Mocha, add chocolate to bottom of the glass, add espresso and mix well, then add milk.</p>
    </article>
    <article class="menu-item">
      <h3 class="menu-item__name">Cappucino | $6</h3>
      <p class="menu-item__desc">Coffee made with milk that has been frothed up with pressurezed steam.</p>
    </article>
    <article class="menu-item">
      <h3 class="menu-item__name">Iced Mocha | $4</h3>
      <p class="menu-item__desc">This served with ice. To make an iced Mocha, add chocolate to bottom of the glass, add espresso and mix well, then add milk.</p>
    </article>
    <article class="menu-item">
      <h3 class="menu-item__name">Cappucino | $6</h3>
      <p class="menu-item__desc">Coffee made with milk that has been frothed up with pressurezed steam.</p>
    </article>
  </div>

  <div class="band"></div>

  <div class="icon-tile icon-tile--left">
    <div class="icon-tile__frame">
      <svg viewBox="0 0 64 64" aria-label="Food icon" role="img">
        <path d="M10 22 L26 56 L34 52 Z" fill="#fff"/>
        <ellipse cx="36" cy="16" rx="6" ry="9" fill="#fff"/>
        <rect x="34.5" y="22" width="3" height="34" fill="#fff"/>
        <path d="M46 8 v12 M50 8 v12 M54 8 v12 M46 20 q4 6 8 0" stroke="#fff" stroke-width="2.2" fill="none"/>
        <rect x="48.5" y="22" width="3" height="34" fill="#fff"/>
      </svg>
    </div>
  </div>

  <div class="icon-tile icon-tile--right">
    <div class="icon-tile__frame">
      <svg viewBox="0 0 64 64" aria-label="Coffee icon" role="img">
        <path d="M28 6 q-5 5 0 10 q5 5 0 10 M36 8 q-4 4 0 8" stroke="#fff" stroke-width="2.5" fill="none" stroke-linecap="round"/>
        <path d="M12 30 H46 V38 Q46 50 29 50 Q12 50 12 38 Z" fill="#fff"/>
        <path d="M46 33 q8 0 6 7 q-2 4 -8 4" stroke="#fff" stroke-width="3" fill="none"/>
        <rect x="8" y="52" width="44" height="4" rx="2" fill="#fff"/>
      </svg>
    </div>
  </div>

  <div class="category category--left">
    <h2 class="category__title">classification here</h2>
    <p class="category__desc">Fillet of fish dipped in our special batter and deep-fried to a golden brown. Served with french fries. (description)</p>
  </div>
  <div class="category category--right">
    <h2 class="category__title">classification here</h2>
    <p class="category__desc">Fillet of fish dipped in our special batter and deep-fried to a golden brown. Served with french fries. (description)</p>
  </div>
</section>

</body>
</html>
```